Buff Works Business card design

i need a business card design for my new detailing company called 'Brent's Detail Shop'. i want an all black and white design . simple, direct and to the point. i want the designer to choose a fitting font to match the logothe front should have logo, address, phone and email and the back side should have a slogan and text indicating that we offer services on anything including cars, trucks, motorcycles and RVs. slogan will read "we take pride in your ride"
maybe also very small on the back side the IG icon with Brents_Detail_Shop

phone 208.474.2863
address 3847 E Larkmoor Ave
Halvern ID 98734
email: BrentsDetail@quorvamail.com

Target Market(s)

all ages , auto enthusiasts

Industry/Entity Type

Automotive

Contact Information for Business Card

the front should have logo, address, phone and email and the back side should have a slogan and text indicating that we offer services on anything including cars, trucks, motorcycles and RVs. slogan will read "we take pride in your ride"

phone 208.474.2863
address 3847 E Larkmoor Ave
Halvern ID 98734

Colors
000000
ffffff

Requirements
Must have
• bold font and very simple design with good spacing
Nice to have
• anything creative from the designer indicating we service any types of vehicles
Should not have
• any colors ,

```html
<!DOCTYPE html>
<html lang="en">
<head>
<meta charset="utf-8">
<title>Brent's Detail Shop – Business Cards</title>
<link href="https://fonts.googleapis.com/css2?family=Roboto+Slab:wght@400;700;800&display=swap" rel="stylesheet">
<style>
  :root {
    --ink: #000000;
    --paper: #ffffff;
    --stage: #2e2a28;
    --card-shadow: rgba(0, 0, 0, 0.45);
  }
  * { margin: 0; padding: 0; box-sizing: border-box; }
  html, body {
    width: 1200px;
    height: 912px;
    overflow: hidden;
    background: var(--stage);
    font-family: "Roboto Slab", serif;
    color: var(--ink);
  }
  .canvas {
    position: relative;
    width: 1200px;
    height: 912px;
  }
  .card {
    position: absolute;
    width: 560px;
    height: 320px;
    background: var(--paper);
    border-radius: 18px;
    box-shadow: 0 10px 24px var(--card-shadow);
    display: flex;
    flex-direction: column;
    align-items: center;
  }
  .card--back { left: 70px; top: 90px; padding-top: 46px; }
  .card--front { left: 570px; top: 500px; padding-top: 34px; }

  .brand-mark {
    display: flex;
    flex-direction: column;
    align-items: center;
    gap: 8px;
  }
  .brand-mark__dot {
    width: 64px;
    height: 64px;
    border-radius: 50%;
    background: var(--ink);
  }
  .brand-mark__name {
    font-weight: 800;
    font-size: 24px;
    letter-spacing: 0.5px;
    color: var(--ink);
  }

  .slogan {
    margin-top: 34px;
    display: flex;
    align-items: center;
    gap: 10px;
    font-size: 14px;
    letter-spacing: 1px;
    text-transform: uppercase;
  }
  .slogan__rule {
    width: 52px;
    height: 1px;
    background: var(--ink);
  }
  .services {
    margin-top: 12px;
    font-size: 17px;
    letter-spacing: 1px;
    text-transform: uppercase;
    padding-top: 10px;
    border-top: 1px solid var(--ink);
  }

  .person {
    margin-top: 22px;
    text-align: center;
  }
  .person__name {
    font-weight: 800;
    font-size: 30px;
    text-transform: uppercase;
    letter-spacing: 0.5px;
    line-height: 1;
  }
  .person__title {
    font-size: 13px;
    margin-top: 4px;
  }
  .person__rule {
    width: 90px;
    height: 1px;
    background: var(--ink);
    margin: 8px auto 0;
  }
  .contact {
    margin-top: 20px;
    text-align: center;
    font-size: 13.5px;
    line-height: 1.75;
    white-space: nowrap;
  }
</style>
</head>
<body>
<main class="canvas">

  <section class="card card--back" aria-label="Card back">
    <div class="brand-mark">
      <span class="brand-mark__dot"></span>
      <span class="brand-mark__name">Brent's Detail Shop</span>
    </div>
    <p class="slogan">
      <span class="slogan__rule"></span>
      We take pride in your ride
      <span class="slogan__rule"></span>
    </p>
    <p class="services">Cars - Trucks - Motorcycles and RVs</p>
  </section>

  <section class="card card--front" aria-label="Card front">
    <div class="brand-mark">
      <span class="brand-mark__dot"></span>
      <span class="brand-mark__name">Brent's Detail Shop</span>
    </div>
    <div class="person">
      <h1 class="person__name">Dorian Vale</h1>
      <p class="person__title">Director</p>
      <div class="person__rule"></div>
    </div>
    <div class="contact">
      <p>P : 208.474.2863 | E : BrentsDetail@quorvamail.com</p>
      <p>W : www.BrentsDetailCo.com | A : 3847 E Larkmoor Ave Halvern ID 98734</p>
    </div>
  </section>

</main>
</body>
</html>
```